real esate business card with company logo and name

we need a business card design for a real esate company

The company name is Walsh & Brody Pty Ltd, and we have our logo designed and will upload. We want classic or moden feel. Black or white background. looks more textured. Should include folowinginformations
Paul Walsh and Lucy Brody
Sales Agents & Onsite Manager
p: 07 5948 2063
F: 07 5948 2174
M:0461 857 239
3/42 Marlin Crescent, MARLOW HEIGHTS QLD 4290

We want this business card looks professonal. Thank you in advance.

Industry/Entity Type

Real Estate Agent

Contact Information for Business Card

Paul Walsh and Lucy Brody
Onsite Manager & Sales Agents
p: 07 5948 2063
M:0461 857 239

Font styles to use
Serif

Colors
000000
fbfbfb
333333
959595

Requirements
Must have
• company logo and name, black or white back ground

```html
<!DOCTYPE html>
<html lang="en">
<head>
<meta charset="utf-8">
<title>Walsh &amp; Brody Pty Ltd – Business Card</title>
<link href="https://fonts.googleapis.com/css2?family=Source+Sans+3:wght@400;600&display=swap" rel="stylesheet">
<style>
  :root{
    --stage:#3a3a3a;
    --card-front:#fbfbfb;
    --card-back:#5a5a5a;
    --ink:#333333;
    --ink-soft:#959595;
    --band-dark:#6f6f6f;
    --band-light:#a9a9a9;
    --white:#ffffff;
  }
  *{margin:0;padding:0;box-sizing:border-box}
  html,body{width:1200px;height:750px;overflow:hidden}
  body{background:var(--stage);font-family:"Source Sans 3",sans-serif;position:relative}
  .card{position:absolute;top:228px;width:461px;height:263px;overflow:hidden}
  .card--front{left:124px;background:var(--card-front);color:var(--ink)}
  .card--back{left:618px;background:linear-gradient(135deg,#616161,var(--card-back) 60%,#555);color:var(--white)}

  .brand-mark{position:absolute;left:346px;top:20px;width:78px;height:78px;background:var(--ink-soft)}
  .brand-name{position:absolute;right:28px;top:126px;font-size:11px;font-weight:600;letter-spacing:.6px;text-transform:uppercase;color:var(--ink)}

  .agents{position:absolute;left:26px;top:133px;font-size:16.5px;font-weight:600;color:#4a4a4a}
  .role{position:absolute;left:26px;top:154px;font-size:11.5px;color:var(--ink-soft)}
  .rule{position:absolute;left:26px;top:174px;width:407px;height:1px;background:#555}

  .contacts{position:absolute;left:26px;top:184px;list-style:none;font-size:10.5px;color:var(--ink)}
  .contacts li{display:flex;align-items:center;gap:6px;height:17.5px}
  .contacts svg{width:12px;height:12px;fill:var(--ink)}

  .address{position:absolute;right:28px;top:203px;text-align:right;font-size:10.5px;line-height:16px;font-style:normal;color:var(--ink)}

  .footer-bands{position:absolute;left:0;bottom:0;width:461px;height:17px}

  .back-name{position:absolute;left:246px;top:125px;font-size:14px;font-weight:600;letter-spacing:1px;text-transform:uppercase}
  .back-url{position:absolute;left:246px;top:145px;font-size:10px;letter-spacing:3.2px}
</style>
</head>
<body>
  <section class="card card--front">
    <div class="brand-mark"></div>
    <div class="brand-name">Walsh &amp; Brody Pty Ltd.</div>

    <h1 class="agents">Paul Walsh &amp; Lucy Brody</h1>
    <p class="role">Sales Agents &amp; Onsite Manager</p>
    <div class="rule"></div>

    <ul class="contacts">
      <li><svg viewBox="0 0 24 24" aria-hidden="true"><path d="M6.6 10.8a15 15 0 0 0 6.6 6.6l2.2-2.2a1 1 0 0 1 1-.25 11.4 11.4 0 0 0 3.6.57 1 1 0 0 1 1 1V20a1 1 0 0 1-1 1A17 17 0 0 1 3 4a1 1 0 0 1 1-1h3.5a1 1 0 0 1 1 1c0 1.25.2 2.45.57 3.57a1 1 0 0 1-.25 1z"/></svg>07 5948 2063</li>
      <li><svg viewBox="0 0 24 24" aria-hidden="true"><path d="M7 1h10a2 2 0 0 1 2 2v18a2 2 0 0 1-2 2H7a2 2 0 0 1-2-2V3a2 2 0 0 1 2-2zm0 3v14h10V4zm5 15.5a1 1 0 1 0 0 2 1 1 0 0 0 0-2z"/></svg>0461 857 239</li>
      <li><svg viewBox="0 0 24 24" aria-hidden="true"><path d="M7 2h10v5H7zM3 8h18a1 1 0 0 1 1 1v8h-4v4H6v-4H2V9a1 1 0 0 1 1-1zm5 8v3h8v-3z"/></svg>07 5948 2174</li>
    </ul>

    <address class="address">3/42 Marlin Crescent<br>MARLOW HEIGHTS QLD 4290</address>

    <svg class="footer-bands" viewBox="0 0 461 17" aria-hidden="true">
      <rect x="0" y="10" width="461" height="7" fill="var(--band-light)"/>
      <rect x="0" y="5" width="346" height="3" fill="var(--band-dark)"/>
      <rect x="376" y="5" width="85" height="3" fill="var(--band-dark)"/>
      <polyline points="346,7 361,1 376,7" fill="none" stroke="var(--band-dark)" stroke-width="2.2"/>
    </svg>
  </section>

  <section class="card card--back">
    <div class="back-name">Walsh &amp; Brody Pty Ltd.</div>
    <div class="back-url">www.walshbrody.com</div>
  </section>
</body>
</html>
```